Business card - mobile service

O KiraTel is a mobile family safety service based on tablets and smartphones.
The business card must have:
BASIC INFO
Company Logo
Name
Position / Job Title: Co-founder
Mobile Phone Number: +55 (11) 5080 6172
Land Line: +55 (11) 9087 614352
Email Address: name@kiratel-example.com
Web Site URL: www.kiratel-example.com
PROMOTIONAL INFO
Try KiraTel free Today!
Your personal promo code: xxxx-2222-uuuu-7777-1234
Promo code text explanation with the instructions about the trial offer
Updates
Dears,
One more must have: the KiraTel slogan:
Industry/Entity Type
Safety
Look and feel
Each slider illustrates characteristics of the customer's brand and the style your logo design should communicate.

```html
<!DOCTYPE html>
<html lang="en">
<head>
<meta charset="utf-8">
<title>KiraTel business card</title>
<link href="https://fonts.googleapis.com/css2?family=Mulish:wght@400;600;800&display=swap" rel="stylesheet">
<style>
  :root{
    --bg:#3b3b3d;
    --sky:#1fa9e1;
    --sky-deep:#1593cc;
    --sun:#f6c10c;
    --amber:#f39a12;
    --paper:#ffffff;
    --pattern:#e6f3fa;
    --ink-soft:#6cc3ea;
  }
  *{box-sizing:border-box;margin:0;padding:0}
  html,body{width:1200px;height:874px;overflow:hidden}
  body{background:var(--bg);font-family:"Mulish",sans-serif;position:relative}
  .card{position:absolute;top:288px;width:520px;height:297px;overflow:hidden;box-shadow:0 12px 30px rgba(0,0,0,.45)}
  .card--front{left:50px;background:linear-gradient(160deg,var(--sky) 0%,var(--sky-deep) 100%)}
  .card--back{left:630px;background:var(--paper)}
  .band{position:absolute;left:0;right:0;bottom:0;height:52px;background:var(--sun);display:flex;align-items:center;padding:0 28px;color:var(--paper);font-size:23px;font-weight:600;letter-spacing:.5px}
  .card--front .band{justify-content:flex-end}
  .card--back .band{justify-content:center}

  .brand{display:flex;align-items:center;gap:10px;font-weight:800;letter-spacing:-1px}
  .brand__dot{width:30px;height:30px;border-radius:50%;background:var(--sun)}
  .card--front .brand{position:absolute;left:36px;top:34px;font-size:58px;color:var(--paper)}
  .slogan{font-weight:800;font-size:21px}
  .slogan__lead{color:var(--sun)}
  .card--front .slogan{position:absolute;left:38px;top:112px;color:var(--paper)}
  .person{position:absolute;left:38px;top:156px;color:var(--paper);font-size:15px}
  .person__sep{margin:0 6px;opacity:.8}
  .contacts{position:absolute;left:38px;top:186px;display:flex;flex-wrap:wrap;gap:9px 22px;width:450px;color:var(--paper);font-size:12.5px}
  .contact{display:flex;align-items:center;gap:6px}
  .contact__icon{width:14px;height:14px;background:var(--sun);border-radius:2px;display:flex;align-items:center;justify-content:center}

  .pattern{position:absolute;left:0;top:0;right:0;bottom:52px;background:linear-gradient(135deg,var(--pattern),var(--paper) 70%)}
  .back-content{position:absolute;left:0;right:0;top:22px;text-align:center}
  .card--back .brand{justify-content:center;font-size:50px;color:var(--sky)}
  .card--back .slogan{color:var(--sky);font-size:16px;margin-top:2px}
  .offer{margin-top:26px;color:var(--sky);font-weight:800;font-size:16px}
  .offer__free{color:var(--amber)}
  .promo{color:var(--sky);font-size:12px;font-weight:600;margin-top:4px;line-height:1.4}
</style>
</head>
<body>
  <section class="card card--front" aria-label="Card front">
    <div class="brand"><span>KiraTel</span><span class="brand__dot"></span></div>
    <p class="slogan"><span class="slogan__lead">Your</span> Family Safety Service</p>
    <p class="person">Marta Quelin<span class="person__sep">|</span>Co-founder</p>
    <div class="contacts">
      <span class="contact"><span class="contact__icon"><svg width="9" height="9" viewBox="0 0 10 10"><path d="M2 1l2 2-1 1.2c.6 1.2 1.6 2.2 2.8 2.8L7 6l2 2-1.3 1.4C4.6 9.2.8 5.4.6 2.3z" fill="#fff"/></svg></span>+55 (11) 5080 6172</span>
      <span class="contact"><span class="contact__icon"><svg width="8" height="10" viewBox="0 0 8 10"><rect x="1" y="0.5" width="6" height="9" rx="1" fill="none" stroke="#fff" stroke-width="1.2"/><circle cx="4" cy="7.6" r=".7" fill="#fff"/></svg></span>+55 (11) 9087 614352</span>
      <span class="contact"><span class="contact__icon"><svg width="10" height="8" viewBox="0 0 10 8"><rect x=".5" y=".5" width="9" height="7" fill="none" stroke="#fff"/><path d="M.5 .8L5 4.5 9.5.8" fill="none" stroke="#fff"/></svg></span>name@kiratel-example.com</span>
    </div>
    <div class="band">www.kiratel-example.com</div>
  </section>

  <section class="card card--back" aria-label="Card back">
    <div class="pattern" role="img" aria-label="Faint repeated brand-name pattern in pale blue"></div>
    <div class="back-content">
      <div class="brand"><span>KiraTel</span><span class="brand__dot"></span></div>
      <p class="slogan"><span class="slogan__lead">Your</span> Family Safety Service</p>
      <p class="offer">Try KiraTel <span class="offer__free">FREE</span> Today!</p>
      <p class="promo">Your personal promo code: XXXX-2222-UUUU-7777-1234<br>Promo code text explanation with the instruction about the trial offer</p>
    </div>
    <div class="band">www.kiratel-example.com</div>
  </section>
</body>
</html>
```